Tallow Crest Business Card

We need a business card designed for a a company called "Tallow Crest". We offer consulting, coaching and training to business leaders and coaches (across the world) using the latest findings in neuroscience, social and emotional intelligence and positive psychology. The final design should communicate the use of brain science to create sustainable relationships.

The card should be doublesided. The logo is attached and names and titles will be provided to the successful designer. Thank you.

Industry/Entity Type

Training

```html
<!DOCTYPE html>
<html lang="en">
<head>
<meta charset="utf-8">
<title>Tallow Crest Business Card</title>
<link rel="stylesheet" href="https://fonts.googleapis.com/css2?family=Source+Sans+3:wght@400;600;700&display=swap">
<style>
  :root {
    --backdrop: #d9dcdf;
    --card-black: #0c0c0d;
    --card-black-soft: #1b1c1e;
    --brand-blue: #1b95d0;
    --brand-lime: #c2d92c;
    --ink-dark: #111111;
    --ink-light: #f2f2f2;
  }
  * { box-sizing: border-box; margin: 0; padding: 0; }
  html, body { width: 1200px; height: 960px; overflow: hidden; }
  body {
    background: var(--backdrop);
    font-family: "Source Sans 3", "Segoe UI", sans-serif;
    position: relative;
  }
  .card {
    position: absolute;
    left: 320px;
    width: 560px;
    height: 320px;
    background: radial-gradient(ellipse at 40% 35%, var(--card-black-soft) 0%, var(--card-black) 70%);
    box-shadow: 0 10px 28px rgba(0,0,0,0.28);
    overflow: hidden;
  }
  .card--front { top: 110px; }
  .card--back  { top: 530px; }

  /* Front */
  .front__bar {
    position: absolute;
    left: 8px; top: 52px;
    width: 26px; height: 232px;
    background: var(--brand-blue);
  }
  .front__brand {
    position: absolute;
    left: 48px; top: 120px;
    width: 200px;
    display: flex; align-items: center; gap: 10px;
  }
  .brand-mark {
    width: 16px; height: 16px;
    background: var(--brand-blue);
    flex: none;
  }
  .brand-name {
    color: var(--brand-blue);
    font-weight: 700;
    font-size: 28px;
    line-height: 1;
    letter-spacing: 0.5px;
  }
  .front__panel {
    position: absolute;
    left: 262px; top: 64px;
    width: 298px; height: 150px;
    background: var(--brand-lime);
    color: var(--ink-dark);
    padding: 12px 22px 0 26px;
  }
  .person__name {
    font-weight: 600;
    font-size: 24px;
    line-height: 1.05;
  }
  .person__title {
    font-size: 14px;
    font-weight: 600;
    margin-left: 118px;
    margin-top: 2px;
  }
  .contact { list-style: none; margin-top: 22px; }
  .contact__item {
    display: flex; align-items: center; gap: 10px;
    font-size: 14px;
    height: 24px;
  }
  .contact__icon { width: 13px; height: 13px; flex: none; }
  .front__address {
    position: absolute;
    right: 22px; top: 228px;
    color: var(--ink-light);
    font-size: 12px;
    text-align: right;
    line-height: 1.25;
  }

  /* Back */
  .back__bar {
    position: absolute;
    top: 46px;
    width: 26px; height: 170px;
    background: var(--brand-lime);
  }
  .back__bar--left { left: 20px; background: var(--brand-lime); }
  .back__bar--right { right: 8px; top: 96px; background: var(--brand-blue); }
  .back__brand {
    position: absolute;
    left: 0; right: 0; top: 138px;
    display: flex; justify-content: center; align-items: center; gap: 12px;
  }
  .back__brand .brand-name { font-size: 36px; }
  .back__brand .brand-mark { width: 20px; height: 20px; }
</style>
</head>
<body>

<section class="card card--front" aria-label="Card front">
  <div class="front__bar"></div>
  <div class="front__brand">
    <span class="brand-mark"></span>
    <span class="brand-name">Tallow Crest</span>
  </div>
  <div class="front__panel">
    <h1 class="person__name">Marcus Hale</h1>
    <p class="person__title">Director</p>
    <ul class="contact">
      <li class="contact__item">
        <svg class="contact__icon" viewBox="0 0 16 16" aria-hidden="true"><path d="M3 1h3l1.5 4-2 1.3a9 9 0 0 0 4.2 4.2L11 8.5l4 1.5v3a2 2 0 0 1-2 2A13 13 0 0 1 1 3a2 2 0 0 1 2-2z" fill="#111"/></svg>
        <span>555-010-482</span>
      </li>
      <li class="contact__item">
        <svg class="contact__icon" viewBox="0 0 16 16" aria-hidden="true"><rect x="1" y="3" width="14" height="10" fill="#111"/><path d="M1.5 3.5 8 9l6.5-5.5" stroke="#c2d92c" stroke-width="1.4" fill="none"/></svg>
        <span>hello@tallowcrest.com</span>
      </li>
      <li class="contact__item">
        <svg class="contact__icon" viewBox="0 0 16 16" aria-hidden="true"><g fill="none" stroke="#111" stroke-width="1.3"><circle cx="8" cy="8" r="6.5"/><ellipse cx="8" cy="8" rx="3" ry="6.5"/><path d="M1.5 8h13M2.5 4.8h11M2.5 11.2h11"/></g></svg>
        <span>www.tallowcrest.com</span>
      </li>
    </ul>
  </div>
  <p class="front__address">Your Complete Address<br>X-Y-Z</p>
</section>

<section class="card card--back" aria-label="Card back">
  <div class="back__bar back__bar--left"></div>
  <div class="back__bar back__bar--right"></div>
  <div class="back__brand">
    <span class="brand-mark"></span>
    <span class="brand-name">Tallow Crest</span>
  </div>
</section>

</body>
</html>
```